We are a company with over 35 years experience supporting our customers IT needs. Implementing wa..*

We want customers to see a strong product line that is covered by our sales and service team.

We sell and service Impact, Mobile and thermal printers. We sell and support fiber optics, data cabling and wireless communications. We manufacture rack labels for warehouse distribution centers and also make shipping labels and private custom labels and all barcode scanning equipment used for receiving, picking and inventory control. We have custom software solutions for WMS and DIstribution Centers.

We support customers like Brindlecart, Fizzora Pop, Grill Monarch, Varnelo, Supermarket chains and 3PL companies.

Looking for a modern design to attract customer who purchase brands we distribute and support. Products from Markwelder, QDV, Inkoval Mobile, RUMEL, Scanworth Scanners, Plexa Networking Equipment to name a few.

Target Market(s)

3PL, Distribution, Bottling Companies, Supermarket Chains, Pharmaceutical

Colors

Designer to choose colors to be used in the design.

Requirements
Must have
• Warehouse Environment or Distribution Center feel.
Nice to have
• Brands we support
Should not have
• Online store feel

```html
<!DOCTYPE html>
<html lang="en">
<head>
<meta charset="utf-8">
<title>IT Services Landing Page</title>
<link href="https://fonts.googleapis.com/css2?family=Poppins:ital,wght@0,300;0,400;0,500;0,600;0,700;1,600&display=swap" rel="stylesheet">
<style>
:root{
  --backdrop:#7ffccf;
  --navy:#172a46;
  --navy-deep:#0f2037;
  --blue:#0a6cf0;
  --blue-bright:#11a8f5;
  --ink:#141c2b;
  --muted:#8a93a3;
  --pale:#eef4fc;
  --line:#e3e8ef;
  --white:#ffffff;
  --star:#f5a623;
}
*{box-sizing:border-box;margin:0;padding:0}
html,body{width:1200px;height:3125px;overflow:hidden}
body{background:var(--backdrop);font-family:'Poppins',sans-serif;color:var(--ink);position:relative}
.page{position:absolute;left:301px;top:129px;width:598px;height:2867px;background:var(--white);overflow:hidden;box-shadow:0 10px 30px rgba(0,0,0,.15)}
.abs{position:absolute}
.photo{position:absolute}
.hero{left:0;top:0;width:598px;height:336px;background:linear-gradient(135deg,#4a5566 0%,#2d3a4d 45%,#3e4858 100%)}
.hero-shade{left:0;top:0;width:598px;height:336px;background:rgba(20,35,60,.55)}
.nav{left:0;top:0;width:598px;height:29px;background:var(--navy-deep)}
.nav a{position:absolute;top:11px;font-size:5.5px;color:#fff;text-decoration:none;font-weight:500;letter-spacing:.2px}
.nav a.active{color:var(--blue-bright)}
.brand{left:254px;top:0;width:90px;height:29px;display:flex;align-items:center;justify-content:center;gap:5px;color:#fff;font-weight:700;font-size:11px}
.brand i{width:9px;height:9px;background:var(--blue);display:block}
.nav-contact{top:10px;font-size:5.5px;color:#fff;display:flex;align-items:center;gap:3px}
.hero-sub{top:103px;width:598px;text-align:center;color:#fff;font-weight:300;font-size:21px}
.hero-title{top:131px;width:598px;text-align:center;color:#fff;font-weight:700;font-size:26px;line-height:31px}
.btn{background:var(--blue);color:#fff;font-size:5.5px;font-weight:500;display:flex;align-items:center;justify-content:center;gap:4px}
.link-under{color:#fff;font-size:6px;text-decoration:underline;font-weight:500}
.feature{background:#fff;box-shadow:0 4px 14px rgba(0,0,0,.08);text-align:center}
.feature.on{background:linear-gradient(180deg,var(--blue-bright),var(--blue));color:#fff}
.icon-ring{margin:0 auto;width:64px;height:64px;border-radius:50%;background:#e6f0fd;display:flex;align-items:center;justify-content:center}
.feature.on .icon-ring{background:rgba(255,255,255,.2)}
.feature h3{font-size:9px;font-weight:600;color:var(--blue);letter-spacing:.3px;line-height:11px}
.feature.on h3{color:#fff}
.feature p{font-size:5.5px;line-height:10px;color:var(--muted);padding:0 14px}
.feature.on p{color:#fff}
.more{font-size:5.5px;color:var(--blue);font-weight:500}
.feature.on .more{color:#fff}
.h2{font-weight:600;font-size:15px;line-height:21px;color:var(--ink)}
.h2 .hl{color:var(--blue)}
.body-s{font-size:5.5px;line-height:10.5px;color:var(--muted)}
.h4{font-size:9px;font-weight:600}
.stats-dark{left:0;top:726px;width:298px;height:232px;background:linear-gradient(135deg,#2a3a52,#1a2b45)}
.stats-pale{left:298px;top:726px;width:300px;height:232px;background:var(--pale)}
.focus h4{font-size:9px;color:#fff;font-weight:600}
.focus p{font-size:5.5px;line-height:10px;color:#c9d2df}
.circle-ico{width:26px;height:26px;border-radius:50%;border:1px solid #4f7fc4;display:flex;align-items:center;justify-content:center}
.stat-num{font-size:17px;font-weight:600}
.stat-lbl{font-size:6px;font-weight:600;color:var(--blue)}
.eyebrow{width:598px;text-align:center;font-size:5.5px;color:var(--blue);font-weight:500}
.center-title{width:598px;text-align:center;font-weight:600;font-size:17px;line-height:23px}
.svc{background:#fff;box-shadow:0 3px 12px rgba(0,0,0,.07);text-align:center}
.svc.on{border:1px solid var(--blue)}
.svc-photo{width:100%;height:61px}
.svc-badge{position:absolute;left:50%;top:45px;margin-left:-16px;width:32px;height:32px;border-radius:50%;background:var(--blue);border:3px solid #5fa5f6;display:flex;align-items:center;justify-content:center}
.svc h5{position:absolute;top:86px;width:100%;font-size:7px;font-weight:600;color:var(--blue);letter-spacing:.2px}
.svc p{position:absolute;top:102px;width:100%;padding:0 10px;font-size:5.5px;line-height:10px;color:var(--muted)}
.svc .go{position:absolute;left:50%;top:143px;margin-left:-8px;width:16px;height:16px;border-radius:50%;border:1px solid #c5ccd6;display:flex;align-items:center;justify-content:center}
.svc.on .go{background:var(--blue);border-color:var(--blue)}
.t-card{border-radius:50%;background:var(--pale)}
.avatar{border-radius:50%;border:1.5px dashed var(--blue);padding:4px;background:#fff}
.avatar div{width:100%;height:100%;border-radius:50%;background:linear-gradient(135deg,#9b7e6a,#3d3431)}
.t-name{font-size:10px;font-weight:600}
.t-role{font-size:5px;color:var(--muted)}
.stars{font-size:6px;color:var(--star);letter-spacing:1px}
.t-quote{font-size:5.5px;line-height:10px;font-weight:600;font-style:italic}
.soc{display:flex;gap:6px}
.soc span{width:14px;height:14px;border-radius:50%;border:1px solid #c5ccd6;background:#fff}
.soc span.on{background:var(--blue);border-color:var(--blue)}
.pager span{display:inline-block;width:16px;height:16px;border-radius:50%;border:1px solid #c5ccd6;margin:0 3px;text-align:center;line-height:14px;font-size:8px;color:var(--muted)}
.contact{left:0;top:1860px;width:598px;height:383px;background:linear-gradient(135deg,#34455e,#1b2c47)}
.contact-shade{left:0;top:1860px;width:598px;height:383px;background:rgba(16,32,56,.45)}
.field{background:#fff;font-size:5.5px;color:var(--muted);padding:7px 10px;height:21px}
.send{background:linear-gradient(90deg,var(--blue),var(--blue-bright));color:#fff;font-size:6px;font-weight:500;text-align:center;line-height:21px}
.map{left:118px;top:2139px;width:362px;height:167px;background:linear-gradient(135deg,#eef1f4,#e3e7ec);box-shadow:0 4px 14px rgba(0,0,0,.12)}
.post{background:#fff;box-shadow:0 3px 14px rgba(0,0,0,.08);padding:18px 15px}
.post h6{font-size:8.5px;font-weight:600;line-height:13px}
.post .date{font-size:5px;color:var(--blue);margin:5px 0 10px}
.author{display:flex;align-items:center;gap:6px;font-size:5.5px;font-weight:500;margin-top:16px}
.author i{width:18px;height:18px;border-radius:50%;background:linear-gradient(135deg,#a05a3c,#3a2a28);display:block}
.footer{left:0;top:2639px;width:598px;height:206px;background:linear-gradient(135deg,#2b3b53,#15263f)}
.footer-shade{left:0;top:2639px;width:598px;height:206px;background:rgba(15,30,55,.5)}
.f-title{font-size:7px;font-weight:600;color:#fff}
.news{display:flex;gap:12px}
.news i{width:24px;height:22px;background:linear-gradient(135deg,#8a6c5c,#3b4b63);display:block;flex:none}
.news p{font-size:5.5px;line-height:9.5px;color:#fff}
.news small{display:block;font-size:4.5px;color:#aeb8c7}
.f-input{border:1px solid #6d7d94;height:20px;font-size:5px;color:#c6cfdb;padding:6px 10px}
.f-btn{background:linear-gradient(90deg,var(--blue),var(--blue-bright));height:20px;color:#fff;font-size:6px;text-align:center;line-height:20px}
.f-soc{display:flex;gap:6px}
.f-soc span{width:13px;height:13px;border-radius:50%;border:1px solid #8190a6}
</style>
</head>
<body>
<main class="page">
  <div class="photo abs hero" role="img" aria-label="Team working together in a bright office"></div>
  <div class="abs hero-shade"></div>
  <nav class="abs nav">
    <a class="active" style="left:65px">HOME</a>
    <a style="left:106px">SERVICES</a>
    <a style="left:159px">ABOUT US</a>
    <a style="left:213px">CONTACT US</a>
    <div class="abs brand"><i></i>Tessel IT</div>
    <div class="abs nav-contact" style="left:356px">
      <svg width="6" height="6" viewBox="0 0 10 10"><path d="M2 1l2 2-1 1.5c.8 1.5 2 2.7 3.5 3.5L8 6.9l2 2L8.7 10C4 9.5.5 6 0 1.3z" fill="#fff"/></svg>+00 123 456 789
    </div>
    <div class="abs nav-contact" style="left:428px;top:9px;font-size:6px">|</div>
    <div class="abs nav-contact" style="left:445px;top:9px">
      <svg width="7" height="5" viewBox="0 0 14 10"><rect width="14" height="10" fill="#fff"/><path d="M0 0l7 5 7-5" stroke="#0f2037" fill="none"/></svg>hello@yoursite.com
    </div>
  </nav>
  <div class="abs hero-sub">IT services built</div>
  <h1 class="abs hero-title">Stop wasting time &amp;<br>money on technology.</h1>
  <div class="abs btn" style="left:236px;top:210px;width:66px;height:18px">All Solution
    <svg width="7" height="5" viewBox="0 0 14 10"><path d="M0 5h12M8 1l4 4-4 4" stroke="#fff" stroke-width="1.6" fill="none"/></svg></div>
  <div class="abs link-under" style="left:318px;top:213px">See live video</div>

  <div class="abs feature" style="left:80px;top:280px;width:146px;height:187px">
    <div class="icon-ring" style="margin-top:20px"><svg width="30" height="30" viewBox="0 0 30 30"><path d="M6 4c4 0 6 6 8 10l10 8-4 5-10-8C6 15 3 8 6 4z" fill="#0a6cf0"/></svg></div>
    <h3 style="margin-top:18px">FIBER OPTICS</h3>
    <p style="margin-top:10px">Lorem ipsum dolor sit amet consectetur adipiscing elit, sed do eiusmod tempor incididunt ut labore.</p>
    <div class="more" style="margin-top:12px">Discover More &nbsp;→</div>
  </div>
  <div class="abs feature on" style="left:226px;top:272px;width:146px;height:202px">
    <div class="icon-ring" style="margin-top:27px"><svg width="34" height="34" viewBox="0 0 34 34"><circle cx="17" cy="17" r="15" stroke="#fff" stroke-width="2" fill="none"/><rect x="13" y="8" width="8" height="12" rx="1" fill="#fff"/><rect x="15" y="20" width="4" height="7" fill="#fff"/></svg></div>
    <h3 style="margin-top:20px">DATA CABLING</h3>
    <p style="margin-top:2px;line-height:8px">Lorm deserm sit coit conetur</p>
    <p style="margin-top:2px">Lorem ipsum dolor sit amet consectetur adipiscing elit, sed do eiusmod tempor incididunt ut labore.</p>
    <div class="more" style="margin-top:12px">Discover More &nbsp;→</div>
  </div>
  <div class="abs feature" style="left:372px;top:280px;width:146px;height:187px">
    <div class="icon-ring" style="margin-top:20px"><svg width="32" height="26" viewBox="0 0 32 26"><path d="M2 9a20 20 0 0 1 28 0M7 14a13 13 0 0 1 18 0M12 19a6 6 0 0 1 8 0" stroke="#0a6cf0" stroke-width="3.5" fill="none" stroke-linecap="round"/><circle cx="16" cy="23" r="2.5" fill="#0a6cf0"/></svg></div>
    <h3 style="margin-top:13px">WIRELESS<br>COMMUNICATIONS</h3>
    <p style="margin-top:4px">Lorem ipsum dolor sit amet consectetur adipiscing elit, sed do eiusmod tempor incididunt ut labore.</p>
    <div class="more" style="margin-top:12px">Discover More &nbsp;→</div>
  </div>

  <h2 class="abs h2" style="left:80px;top:524px">We have over <span class="hl">35+</span><br>years experience.</h2>
  <p class="abs body-s" style="left:80px;top:571px;width:230px">Ut enim ad minim veniam, quis nostrud exercitation ullamco laboris nisi ut aliquip commodo consequat. Duis aute irure dolor in reprehenderit in voluptate velit ess cillum dolore eu fugiat nulla pariatur.</p>
  <div class="abs h4" style="left:80px;top:614px">Our Mission</div>
  <p class="abs body-s" style="left:80px;top:631px;width:105px">Ut enim minim veniam quis nostrud exercitation ullamco laboris ut aliqu commodo consequat. Duis aute iru fugiat nulla pariatur.</p>
  <div class="abs h4" style="left:205px;top:614px">Our Vission</div>
  <p class="abs body-s" style="left:205px;top:631px;width:105px">Ut enim minim veniam quis nostrud exercitation ullamco laboris ut aliqu commodo consequat. Duis aute iru fugiat nulla pariatur.</p>
  <div class="photo" style="left:341px;top:520px;width:176px;height:75px;background:linear-gradient(135deg,#b78c72,#5b4a44)" role="img" aria-label="Colleagues meeting around a table"></div>
  <div class="photo" style="left:341px;top:605px;width:82px;height:76px;background:linear-gradient(135deg,#c9a060,#4c3e36)" role="img" aria-label="Two people looking at a laptop"></div>
  <div class="photo" style="left:435px;top:605px;width:82px;height:76px;background:linear-gradient(135deg,#6d5a4e,#2a2422)" role="img" aria-label="Woman reading a phone at a desk"></div>
  <div class="abs" style="left:407px;top:580px;width:42px;height:42px;border-radius:50%;background:var(--blue);display:flex;align-items:center;justify-content:center"><svg width="9" height="10" viewBox="0 0 9 10"><path d="M0 0l9 5-9 5z" fill="#fff"/></svg></div>

  <div class="photo abs stats-dark" role="img" aria-label="Engineers working at computers"></div>
  <div class="abs stats-pale"></div>
  <div class="abs focus" style="left:106px;top:757px;width:175px">
    <div class="circle-ico"><svg width="12" height="12" viewBox="0 0 12 12"><path d="M6 1l5 9H1z" stroke="#4f9cf5" fill="none"/></svg></div>
    <h4 style="margin-top:6px">Focus on your business</h4>
    <p style="margin-top:5px">Deploying a Corelane computer network solution to address what ails your business technology can get you back your competitive advantage and help you grow your business again.</p>
  </div>
  <div class="abs focus" style="left:106px;top:849px;width:175px">
    <div class="circle-ico" style="background:#2d5b9a"><svg width="12" height="12" viewBox="0 0 12 12"><rect x="2" y="2" width="8" height="8" stroke="#8fc0ff" fill="none"/></svg></div>
    <h4 style="margin-top:6px">We take care of your technology</h4>
    <p style="margin-top:5px">Deploying a Corelane computer network solution to address what ails your business technology can get you back your competitive advantage and help you grow your business again.</p>
  </div>
  <div class="abs" style="left:426px;top:773px;width:1px;height:58px;background:#d5dde8"></div>
  <div class="abs" style="left:426px;top:851px;width:1px;height:58px;background:#d5dde8"></div>
  <div class="abs" style="left:334px;top:774px"><svg width="14" height="14" viewBox="0 0 14 14"><circle cx="5" cy="4" r="2.5" stroke="#0a6cf0" fill="none"/><circle cx="10" cy="4" r="2.5" stroke="#0a6cf0" fill="none"/><path d="M1 12c0-3 8-3 8 0M6 12c0-3 7-3 7 0" stroke="#0a6cf0" fill="none"/></svg>
    <div class="stat-num" style="margin-top:6px">8565</div><div class="stat-lbl">Happy Clients</div></div>
  <div class="abs" style="left:462px;top:774px"><svg width="14" height="14" viewBox="0 0 14 14"><rect x="2" y="1" width="10" height="12" stroke="#0a6cf0" fill="none"/><path d="M4 7l2 2 4-4" stroke="#0a6cf0" fill="none"/></svg>
    <div class="stat-num" style="margin-top:6px">934</div><div class="stat-lbl">Finished Project</div></div>
  <div class="abs" style="left:334px;top:855px"><svg width="14" height="14" viewBox="0 0 14 14"><circle cx="7" cy="7" r="3" stroke="#0a6cf0" fill="none"/><path d="M7 1v3M7 10v3M1 7h3M10 7h3" stroke="#0a6cf0"/></svg>
    <div class="stat-num" style="margin-top:6px">534</div><div class="stat-lbl">Skilled Experts</div></div>
  <div class="abs" style="left:462px;top:855px"><svg width="14" height="14" viewBox="0 0 14 14"><rect x="1" y="2" width="12" height="9" stroke="#0a6cf0" fill="none"/><path d="M4 13h6" stroke="#0a6cf0"/></svg>
    <div class="stat-num" style="margin-top:6px">438</div><div class="stat-lbl">Media Posts</div></div>

  <div class="abs eyebrow" style="top:999px">Services</div>
  <h2 class="abs center-title" style="top:1016px">Managed IT services<br>for your industry</h2>

  <div class="abs svc" style="left:80px;top:1093px;width:101px;height:170px">
    <div class="svc-photo" style="background:linear-gradient(135deg,#7a6656,#2f2a2a)" role="img" aria-label="Team collaborating in a workshop"></div>
    <div class="svc-badge"><svg width="14" height="14" viewBox="0 0 14 14"><path d="M7 1l5 2v4c0 3-2 5-5 6-3-1-5-3-5-6V3z" stroke="#fff" fill="none"/></svg></div>
    <h5>RACK LABELS</h5><p>Protect your business from malware, hackers, viruses security.</p>
    <div class="go"><svg width="7" height="5" viewBox="0 0 14 10"><path d="M0 5h12M8 1l4 4-4 4" stroke="#8a93a3" stroke-width="1.6" fill="none"/></svg></div></div>
  <div class="abs svc on" style="left:193px;top:1093px;width:99px;height:170px">
    <div class="svc-photo" style="background:linear-gradient(135deg,#c08f74,#4a4a52)" role="img" aria-label="Two colleagues at a laptop"></div>
    <div class="svc-badge"><svg width="14" height="14" viewBox="0 0 14 14"><circle cx="4" cy="4" r="2" stroke="#fff" fill="none"/><circle cx="10" cy="4" r="2" stroke="#fff" fill="none"/><circle cx="4" cy="10" r="2" stroke="#fff" fill="none"/><circle cx="10" cy="10" r="2" stroke="#fff" fill="none"/></svg></div>
    <h5>SHIPPING LABELS</h5><p>Protect your business from malware, hackers, viruses security.</p>
    <div class="go"><svg width="7" height="5" viewBox="0 0 14 10"><path d="M0 5h12M8 1l4 4-4 4" stroke="#fff" stroke-width="1.6" fill="none"/></svg></div></div>
  <div class="abs svc" style="left:304px;top:1093px;width:99px;height:170px">
    <div class="svc-photo" style="background:linear-gradient(135deg,#8d9097,#262a33)" role="img" aria-label="People meeting in a glass office"></div>
    <div class="svc-badge"><svg width="14" height="14" viewBox="0 0 14 14"><circle cx="7" cy="3" r="2" fill="#fff"/><circle cx="3" cy="11" r="2" fill="#fff"/><circle cx="11" cy="11" r="2" fill="#fff"/><path d="M7 5v3M7 8L3 9M7 8l4 1" stroke="#fff"/></svg></div>
    <h5>PRIVATE CUSTOM LABELS</h5><p>Protect your business from malware, hackers, viruses security.</p>
    <div class="go"><svg width="7" height="5" viewBox="0 0 14 10"><path d="M0 5h12M8 1l4 4-4 4" stroke="#8a93a3" stroke-width="1.6" fill="none"/></svg></div></div>
  <div class="abs svc" style="left:416px;top:1093px;width:101px;height:170px">
    <div class="svc-photo" style="background:linear-gradient(135deg,#d3c4aa,#6e5a4a)" role="img" aria-label="Team seated in a bright lounge"></div>
    <div class="svc-badge"><svg width="14" height="14" viewBox="0 0 14 14"><rect x="2" y="2" width="10" height="10" stroke="#fff" fill="none"/><path d="M4 5h6M4 7h6M4 9h6" stroke="#fff"/></svg></div>
    <h5>BARCODE SCANNING</h5><p>Protect your business from malware, hackers, viruses security.</p>
    <div class="go"><svg width="7" height="5" viewBox="0 0 14 10"><path d="M0 5h12M8 1l4 4-4 4" stroke="#8a93a3" stroke-width="1.6" fill="none"/></svg></div></div>

  <div class="abs svc" style="left:80px;top:1275px;width:101px;height:170px">
    <div class="svc-photo" style="background:linear-gradient(135deg,#5c6e82,#2a2c33)" role="img" aria-label="Developers working at screens"></div>
    <div class="svc-badge"><svg width="14" height="14" viewBox="0 0 14 14"><rect x="1" y="2" width="12" height="9" stroke="#fff" fill="none"/><path d="M3 9l3-3 2 2 3-3" stroke="#fff" fill="none"/></svg></div>
    <h5>CUSTOM SOFTWARE</h5><p>Protect your business from malware, hackers, viruses security.</p>
    <div class="go"><svg width="7" height="5" viewBox="0 0 14 10"><path d="M0 5h12M8 1l4 4-4 4" stroke="#8a93a3" stroke-width="1.6" fill="none"/></svg></div></div>
  <div class="abs svc" style="left:193px;top:1275px;width:99px;height:170px">
    <div class="svc-photo" style="background:linear-gradient(135deg,#d9d3cb,#7a6d66)" role="img" aria-label="Colleagues discussing in an office"></div>
    <div class="svc-badge"><svg width="14" height="14" viewBox="0 0 14 14"><path d="M7 1l5 2v4c0 3-2 5-5 6-3-1-5-3-5-6V3z" stroke="#fff" fill="none"/><path d="M5 7l2 2 3-3" stroke="#fff" fill="none"/></svg></div>
    <h5>THERMAL PRINTERS</h5><p>Protect your business from malware, hackers, viruses security.</p>
    <div class="go"><svg width="7" height="5" viewBox="0 0 14 10"><path d="M0 5h12M8 1l4 4-4 4" stroke="#8a93a3" stroke-width="1.6" fill="none"/></svg></div></div>
  <div class="abs svc" style="left:304px;top:1275px;width:99px;height:170px">
    <div class="svc-photo" style="background:linear-gradient(135deg,#7a4a9a,#2b2c45)" role="img" aria-label="Man at a desk in a dark studio"></div>
    <div class="svc-badge"><svg width="14" height="14" viewBox="0 0 14 14"><circle cx="7" cy="7" r="5" stroke="#fff" fill="none"/><path d="M7 4v3l2 2" stroke="#fff" fill="none"/></svg></div>
    <h5>SCANWORTH SCANNERS</h5><p>Protect your business from malware, hackers, viruses security.</p>
    <div class="go"><svg width="7" height="5" viewBox="0 0 14 10"><path d="M0 5h12M8 1l4 4-4 4" stroke="#8a93a3" stroke-width="1.6" fill="none"/></svg></div></div>
  <div class="abs svc" style="left:416px;top:1275px;width:101px;height:170px">
    <div class="svc-photo" style="background:linear-gradient(135deg,#b9b1a2,#4c4a48)" role="img" aria-label="Workstations in an open office"></div>
    <div class="svc-badge"><svg width="14" height="14" viewBox="0 0 14 14"><rect x="2" y="1" width="10" height="12" stroke="#fff" fill="none"/><path d="M4 4h6M4 7h6M4 10h4" stroke="#fff"/></svg></div>
    <h5>INKOVAL MOBILE</h5><p>Protect your business from malware, hackers, viruses security.</p>
    <div class="go"><svg width="7" height="5" viewBox="0 0 14 10"><path d="M0 5h12M8 1l4 4-4 4" stroke="#8a93a3" stroke-width="1.6" fill="none"/></svg></div></div>

  <div class="abs eyebrow" style="top:1495px">Testimonial</div>
  <h2 class="abs" style="top:1512px;width:598px;text-align:center;font-size:11px;font-weight:700;line-height:14px;letter-spacing:.3px">WHAT PEOPLE SAY<br>ABOUT OUR SERVICES</h2>

  <div class="abs t-card" style="left:80px;top:1584px;width:211px;height:214px"></div>
  <div class="abs avatar" style="left:80px;top:1584px;width:76px;height:76px"><div role="img" aria-label="Client portrait"></div></div>
  <div class="abs t-name" style="left:170px;top:1608px">Lin Haoyu</div>
  <div class="abs t-role" style="left:170px;top:1627px">Marketing Officer</div>
  <div class="abs stars" style="left:170px;top:1637px">★★★★★</div>
  <p class="abs t-quote" style="left:105px;top:1675px;width:170px">Ut enim minim veniam quis nostrud exercitation ullam commodo consequat sint sunt in culpa.</p>
  <p class="abs body-s" style="left:105px;top:1700px;width:170px">Ut enim ad minim veniam, quis nostrud exercitation ullamco commodo consequat is aute irure in reprehenderit voluptat proident, sunt in culpa qui officia deserunt Ut enim minim irure in reprehenderit voluptat.</p>
  <div class="abs soc" style="left:149px;top:1756px"><span></span><span class="on"></span><span></span><span></span></div>

  <div class="abs t-card" style="left:304px;top:1584px;width:212px;height:214px"></div>
  <div class="abs avatar" style="left:304px;top:1584px;width:76px;height:76px"><div role="img" aria-label="Client portrait"></div></div>
  <div class="abs t-name" style="left:394px;top:1608px">Mei Soran</div>
  <div class="abs t-role" style="left:394px;top:1627px">Marketing Officer</div>
  <div class="abs stars" style="left:394px;top:1637px">★★★★★</div>
  <p class="abs t-quote" style="left:329px;top:1675px;width:170px">Ut enim minim veniam quis nostrud exercitation ullam commodo consequat sint sunt in culpa.</p>
  <p class="abs body-s" style="left:329px;top:1700px;width:170px">Ut enim ad minim veniam, quis nostrud exercitation ullamco commodo consequat is aute irure in reprehenderit voluptat proident, sunt in culpa qui officia deserunt Ut enim minim irure in reprehenderit voluptat.</p>
  <div class="abs soc" style="left:373px;top:1756px"><span></span><span class="on"></span><span></span><span></span></div>

  <div class="abs pager" style="left:276px;top:1799px"><span>←</span><span>→</span></div>

  <div class="photo abs contact" role="img" aria-label="Engineer working at a desk in a dim office"></div>
  <div class="abs contact-shade"></div>
  <div class="abs eyebrow" style="top:1904px">Contact Us</div>
  <h2 class="abs center-title" style="top:1918px;color:#fff">Get in touch<br>We'll help your <span style="color:var(--blue)">IT solution</span></h2>
  <div class="abs field" style="left:118px;top:1998px;width:176px">First Name</div>
  <div class="abs field" style="left:118px;top:2029px;width:176px">Last Name</div>
  <div class="abs field" style="left:118px;top:2059px;width:176px">Email Address</div>
  <div class="abs field" style="left:118px;top:2090px;width:176px">Phone No.</div>
  <div class="abs field" style="left:304px;top:1998px;width:176px;height:84px">Message here</div>
  <div class="abs send" style="left:304px;top:2090px;width:176px;height:21px">Send Message Now</div>
  <div class="abs map" role="img" aria-label="Street map with a location pin"></div>
  <svg class="abs" style="left:290px;top:2199px" width="18" height="24" viewBox="0 0 18 24"><path d="M9 0a9 9 0 0 1 9 9c0 6-9 15-9 15S0 15 0 9a9 9 0 0 1 9-9z" fill="#0a6cf0"/><circle cx="9" cy="9" r="3.5" fill="#fff"/></svg>

  <div class="abs eyebrow" style="top:2350px">Blog Post</div>
  <h2 class="abs center-title" style="top:2367px">The latest on innovation<br>&amp; industry trends</h2>
  <div class="abs post" style="left:80px;top:2441px;width:134px;height:151px">
    <h6>Let us provide the<br>support you deserve.</h6><div class="date">02 January, 2020</div>
    <p class="body-s">Minim veniam, quis nostrud exercitatio ullamco commodo consequat is aute irure in reprehenderit voluptat proide reprehen derit volupat.</p>
    <div class="author"><i role="img" aria-label="Author portrait"></i>By Dorian Fell</div></div>
  <div class="abs post" style="left:229px;top:2441px;width:139px;height:151px">
    <h6>Let us provide the<br>support you deserve.</h6><div class="date">02 January, 2020</div>
    <p class="body-s">Minim veniam, quis nostrud exercitatio ullamco commodo consequat is aute irure in reprehenderit voluptat proide reprehen derit volupat.</p>
    <div class="author"><i role="img" aria-label="Author portrait"></i>By Dorian Fell</div></div>
  <div class="abs post" style="left:379px;top:2441px;width:138px;height:151px">
    <h6>Let us provide the<br>support you deserve.</h6><div class="date">02 January, 2020</div>
    <p class="body-s">Minim veniam, quis nostrud exercitatio ullamco commodo consequat is aute irure in reprehenderit voluptat proide reprehen derit volupat.</p>
    <div class="author"><i role="img" aria-label="Author portrait"></i>By Dorian Fell</div></div>

  <div class="photo abs footer" role="img" aria-label="Office team at work, darkened"></div>
  <div class="abs footer-shade"></div>
  <div class="abs f-title" style="left:255px;top:2683px">Lastest News</div>
  <div class="abs" style="left:255px;top:2709px;width:130px;display:flex;flex-direction:column;gap:15px">
    <div class="news"><i role="img" aria-label="News thumbnail"></i><p>Improving lives technology lighthouse project<small>May 26, 2020</small></p></div>
    <div class="news"><i role="img" aria-label="News thumbnail"></i><p>Improving lives technology lighthouse project<small>May 26, 2020</small></p></div>
    <div class="news"><i role="img" aria-label="News thumbnail"></i><p>Improving lives technology lighthouse project<small>May 26, 2020</small></p></div>
  </div>
  <div class="abs f-title" style="left:405px;top:2683px">Subscribe Us</div>
  <div class="abs f-input" style="left:405px;top:2709px;width:112px">Email Here</div>
  <div class="abs f-btn" style="left:405px;top:2738px;width:112px">Send Now</div>
  <div class="abs f-soc" style="left:408px;top:2773px"><span></span><span></span><span></span><span></span></div>
</main>
</body>
</html>
```